Webdesign for Non profit Diabetes education company

We are looking for a website design for our company.

We just created the company Glucose Guidance Circle

The concept for the company is to educate diabetics with resources that will help them manage their Diabetes. The list of advisers will be dietitians, podiatrist, diabetic educators, and fitness centers.

Please see attached logo. I like the logo to include an image that connects people together.

I've attached our logo, please use the colors in the design of the site.

Creativity is encouraged. Have fun with this project. We are looking for a professional site but not to corporate.

The page must be written in HTML 5 and be responsive built for mobile. You can use bootstrap, jquery, or angular JS.

Wordpress or wix will not be accepted.

The website will be hosted at www.glucoseguidancecircle.example

Requirements
Must have
• The page must be written in HTML 5 and be responsive built for mobile. You can use bootstrap, jquery, or angular JS.
• The landing page should include a splash page. Please incorporate the logo and the
Should not have
• Wordpress or wix will not be accepted.

```html
<!DOCTYPE html>
<html lang="en">
<head>
<meta charset="utf-8">
<title>Glucose Guidance Circle</title>
<link href="https://fonts.googleapis.com/css2?family=Oswald:wght@400;500&family=Roboto:wght@400;500;700&display=swap" rel="stylesheet">
<style>
:root{
  --pink:#f0628d;
  --pink-soft:#f48aaa;
  --blue:#6d8fcf;
  --blue-deep:#5b7dc2;
  --navy:#1f2b45;
  --text:#444;
  --muted:#999;
  --line:#e3e3e3;
  --grey-bg:#efefef;
  --field:#eeeeee;
  --footer:#1d1d1f;
  --white:#fff;
}
*{box-sizing:border-box;margin:0;padding:0}
html,body{width:1200px;height:3727px;overflow:hidden}
body{font-family:"Roboto",Arial,sans-serif;color:var(--text);background:var(--white);position:relative}
.abs{position:absolute}
.heading{font-family:"Oswald","Arial Narrow",sans-serif;font-weight:500;text-transform:uppercase;letter-spacing:.5px}
.pink{color:var(--pink)}.blue{color:var(--blue)}

/* header */
.site-header{position:absolute;left:0;top:0;width:1200px;height:107px;background:var(--white)}
.brand{position:absolute;left:222px;top:22px;display:flex;align-items:center;gap:10px}
.brand-dot{width:40px;height:40px;border-radius:50%;background:var(--blue)}
.brand-name{font-family:"Roboto",sans-serif;font-weight:700;font-size:15px;color:var(--pink);line-height:1.2;width:150px}
.topline{position:absolute;left:395px;top:8px;width:605px;border-bottom:1px solid var(--line);height:24px;display:flex;justify-content:flex-end;gap:18px;font-size:11px;color:#666;align-items:center}
.topline .soc{display:flex;gap:10px}
.topline .soc span{width:10px;height:10px;background:#777;display:block}
.contactline{position:absolute;left:395px;top:42px;width:605px;display:flex;gap:60px;font-size:11px;color:#333;align-items:center;padding-left:60px}
.contactline b{display:block;font-weight:500}
.appt{margin-left:auto;border:1px solid #555;padding:7px 20px;font-size:11px;font-weight:700}

.nav{position:absolute;top:107px;left:0;width:1200px;height:47px;background:var(--blue)}
.nav-pink{position:absolute;left:0;top:0;width:720px;height:47px;background:linear-gradient(90deg,var(--pink),var(--pink-soft));clip-path:polygon(0 0,100% 0,96% 100%,0 100%)}
.nav ul{position:absolute;left:200px;top:15px;display:flex;gap:22px;list-style:none;color:var(--white);font-size:12px;font-weight:500}
.nav li:first-child{border-bottom:2px solid var(--white);padding-bottom:4px}
.search{position:absolute;left:775px;top:10px;width:225px;border-bottom:1px solid rgba(255,255,255,.8);color:var(--white);font-size:12px;padding:4px 0;display:flex;justify-content:space-between}

/* hero */
.hero{position:absolute;top:154px;left:0;width:1200px;height:487px;overflow:hidden}
.hero-photo{position:absolute;inset:0;background:linear-gradient(120deg,#c9ccd2,#eaeaea 55%,#d8cdc6)}
.hero-overlay{position:absolute;left:0;top:0;width:745px;height:487px;background:linear-gradient(160deg,rgba(109,143,207,.95),rgba(91,125,194,.9));clip-path:polygon(0 0,100% 0,75% 100%,0 100%)}
.hero h1{position:absolute;left:200px;top:85px;font-size:54px;line-height:1.2;color:var(--white)}
.hero h1 span{color:var(--navy)}
.hero p{position:absolute;left:200px;top:230px;width:440px;font-size:14px;line-height:1.6;color:var(--white)}
.btn-white{position:absolute;background:var(--white);color:var(--pink);font-size:12px;font-weight:700;padding:14px 32px}
.btn-outline{position:absolute;border:1px solid var(--white);color:var(--white);font-size:12px;padding:13px 28px}
.hero-arrows{position:absolute;left:540px;top:435px;display:flex}
.hero-arrows span{width:50px;height:52px;display:flex;align-items:center;justify-content:center;color:var(--white);font-size:20px}

/* mission */
.mission{position:absolute;top:641px;left:0;width:1200px;height:241px}
.sec-mark{width:50px;height:50px;border-radius:50%;border:4px solid var(--blue);display:inline-block}
.mission .title{position:absolute;left:200px;top:62px;display:flex;align-items:center;gap:12px;font-size:24px}
.mission .rule{position:absolute;left:200px;top:128px;width:800px;border-top:1px solid var(--line)}
.mission p{position:absolute;left:200px;top:142px;width:800px;font-size:13px;line-height:1.6;color:#333}

/* facts */
.facts{position:absolute;top:882px;left:0;width:1200px;height:484px;background:linear-gradient(135deg,#f4f4f4,#e8e8e8)}
.center-title{position:absolute;left:0;width:1200px;display:flex;justify-content:center;align-items:center;gap:12px;font-size:24px}
.facts p.lead{position:absolute;left:235px;top:130px;width:730px;text-align:center;font-size:13px;line-height:1.6;color:#333}
.fact-card{position:absolute;top:243px;width:241px;height:216px;background:linear-gradient(160deg,var(--pink) 10%,var(--blue) 100%);color:var(--white);text-align:center;padding-top:70px}
.fact-icon{position:absolute;left:95px;top:-25px;width:52px;height:52px;border-radius:50%;background:var(--white);border:3px solid #eee}
.fact-icon::after{content:"";position:absolute;left:16px;top:12px;width:14px;height:20px;border:2px solid #555;border-radius:3px}
.fact-card h3{font-family:"Oswald",sans-serif;font-weight:500;font-size:15px;margin-bottom:8px}
.fact-card p{font-size:12px;line-height:1.5;padding:0 26px}

/* network */
.network{position:absolute;top:1366px;left:0;width:1200px;height:584px;overflow:hidden}
.network h2{position:absolute;left:0;top:118px;width:1200px;text-align:center;font-size:30px;line-height:1.3}
.node{position:absolute;width:230px;font-size:11px;line-height:1.5;color:var(--muted)}
.node b{display:block;font-family:"Oswald",sans-serif;font-weight:500;color:var(--navy);font-size:12px;text-transform:uppercase}

/* government */
.gov{position:absolute;top:1950px;left:0;width:1200px;height:646px;overflow:hidden}
.gov-photo{position:absolute;inset:0;background:linear-gradient(100deg,#c7b3a4,#ddd3cc 40%,#bfc3c9 70%,#d7d9dc)}
.gov-box{position:absolute;left:572px;top:0;width:428px;height:205px;background:var(--blue);color:var(--white);padding:22px 26px;font-size:26px;line-height:1.3}
.svc{position:absolute;background:var(--white);box-shadow:0 2px 6px rgba(0,0,0,.12);font-size:11px;line-height:1.5;color:#666}
.svc h4{font-family:"Oswald",sans-serif;font-weight:500;font-size:13px;color:var(--navy);text-align:right;text-transform:uppercase;margin-bottom:8px}
.svc .chev{position:absolute;left:8px;top:38px;color:#888;font-size:16px}

/* newsletter */
.newsletter{position:absolute;top:2596px;left:0;width:1200px;height:199px;background:linear-gradient(100deg,var(--pink) 0%,#f59db6 100%)}
.newsletter .title{position:absolute;left:200px;top:50px;display:flex;gap:18px;align-items:center;color:var(--white);font-size:26px;line-height:1.1}
.nl-field{position:absolute;top:52px;height:44px;border:1px solid rgba(255,255,255,.85);color:var(--white);font-size:12px;padding:14px 10px}
.nl-send{position:absolute;left:668px;top:112px;width:162px;height:44px;background:var(--pink);border:1px solid rgba(255,255,255,.6);color:var(--white);font-size:13px;font-weight:700;text-align:center;line-height:42px}

/* pro signup */
.pro{position:absolute;top:2795px;left:0;width:1200px;height:347px;border-bottom:1px solid var(--line)}
.field{position:absolute;height:42px;background:var(--field);font-size:12px;color:#333;padding:14px 12px}
.submit{position:absolute;left:538px;top:257px;width:126px;height:38px;background:var(--blue);color:var(--white);text-align:center;line-height:38px;font-size:12px;font-weight:700}

/* blog */
.blog{position:absolute;top:3142px;left:0;width:1200px;height:398px}
.post{position:absolute;top:120px;width:240px}
.post-img{height:92px;margin-left:44px;background:linear-gradient(120deg,#b9c3cf,#e3ddd8)}
.post-date{position:absolute;left:0;top:0;width:44px;height:58px;background:var(--white);border:1px solid var(--line);font-size:10px;text-align:center;padding-top:8px;color:#666}
.post-date i{position:absolute;left:0;bottom:-36px;width:44px;height:36px;background:var(--blue)}
.post h5{margin-top:14px;font-size:14px;font-weight:700;color:#222}
.post p{font-size:12px;line-height:1.5;color:#555;margin-top:6px}
.post .more{border-top:1px solid var(--line);margin-top:12px;padding-top:12px;display:flex;justify-content:flex-end}
.post .more span{border:1px solid #bbb;font-size:11px;padding:5px 10px}
.post .more span.on{background:var(--blue);color:var(--white);border-color:var(--blue)}

/* footer */
.footer{position:absolute;top:3540px;left:0;width:1200px;height:187px;background:var(--footer);color:#ddd;font-size:12px;line-height:1.7}
.footer h6{font-family:"Oswald",sans-serif;font-weight:500;font-size:14px;color:var(--white);margin-bottom:14px;text-transform:uppercase}
.f-soc{display:flex;gap:8px;margin-top:10px}
.f-soc span{width:20px;height:20px;display:block}
</style>
</head>
<body>

<header class="site-header">
  <div class="brand"><span class="brand-dot"></span><span class="brand-name">Glucose Guidance Circle</span></div>
  <div class="topline">
    <span>&#9993; info@glucoseguidancecircle.example</span>
    <span>Sign Up</span>
    <span>Language &#9662;</span>
    <span class="soc"><span></span><span></span><span></span><span></span></span>
  </div>
  <div class="contactline">
    <span>&#9990; <b>Call Us</b>+1 555 014 7788</span>
    <span>&#9679; <b>Location</b>Lorem Ipsum is dummy text here.</span>
    <span class="appt">APPOINTMENT</span>
  </div>
</header>

<nav class="nav">
  <div class="nav-pink"></div>
  <ul><li>Home</li><li>Find a healthcare provider</li><li>Join our network</li><li>Newsletter</li><li>Blog</li></ul>
  <div class="search"><span>Search</span><span>&#9906;</span></div>
</nav>

<section class="hero">
  <div class="hero-photo" role="img" aria-label="Close-up photo of a hand testing blood glucose with a meter"></div>
  <div class="hero-overlay"></div>
  <h1 class="heading">Glucose Guidance<br><span>Circle.</span></h1>
  <p>Diabetes occurs when your blood glucose, also called blood sugar, is too high. High blood glucose can cause health..</p>
  <span class="btn-white" style="left:200px;top:312px">CONTACT US</span>
  <span class="btn-outline" style="left:343px;top:312px">LEARN MORE</span>
  <div class="hero-arrows"><span style="background:var(--navy)">&larr;</span><span style="background:var(--blue)">&rarr;</span></div>
</section>

<section class="mission">
  <div class="title heading"><span class="sec-mark"></span><span class="pink">Mission <span class="blue">Statement</span></span></div>
  <div class="rule"></div>
  <p>"At the Glucose Guidance Circle, our focus is to connect newly diagnosed and existing patients with diabetes to a network of available professionals who possess the knowledge to manage your diabetes."</p>
</section>

<section class="facts">
  <div class="center-title heading" style="top:58px"><span class="sec-mark"></span><span class="pink">Diabetes Facts <span class="blue">and Statistics</span></span></div>
  <p class="lead">Diabetes occurs when your blood glucose, also called blood sugar, is too high. High blood glucose can cause health problems over time. The main types of diabetes are type 1, type 2, and gestational</p>
  <div class="fact-card" style="left:201px"><span class="fact-icon"></span><h3>TOTAL</h3><p>An estimated 30.3 million people have diabetes (9.4 percent of the U.S. population)</p></div>
  <div class="fact-card" style="left:480px"><span class="fact-icon"></span><h3>DIAGNOSED</h3><p>An estimated 23.1 million people have been diagnosed with diabetes (7.2 percent of the U.S. population)</p></div>
  <div class="fact-card" style="left:760px"><span class="fact-icon"></span><h3>UNDIAGNOSED</h3><p>An estimated 7.2 million adults, ages 18 years or older are undiagnosed (23.8 percent of people with diabetes)</p></div>
</section>

<section class="network">
  <span class="sec-mark abs" style="left:575px;top:60px"></span>
  <h2 class="heading"><span class="pink">Our network of healthcare providers will help</span><br><span class="pink">you manage</span> <span class="blue">your diabetes.</span></h2>
  <svg class="abs" style="left:380px;top:310px" width="440" height="270" viewBox="0 0 440 270">
    <defs><linearGradient id="arcGrad" x1="0" x2="1"><stop offset="0" stop-color="#f0628d"/><stop offset="1" stop-color="#6d8fcf"/></linearGradient></defs>
    <path d="M20 250 A200 200 0 0 1 420 250" fill="none" stroke="url(#arcGrad)" stroke-width="3"/>
    <circle cx="220" cy="50" r="5" fill="#6d8fcf"/>
    <circle cx="78" cy="108" r="5" fill="#6d8fcf"/>
    <circle cx="362" cy="108" r="5" fill="#6d8fcf"/>
    <circle cx="28" cy="200" r="5" fill="#6d8fcf"/>
    <circle cx="412" cy="200" r="5" fill="#6d8fcf"/>
  </svg>
  <div class="node" style="left:485px;top:235px;text-align:center"><b>Endocrinologist</b>a physician who specializes in treating disorders of the endocrine...</div>
  <div class="node" style="left:200px;top:320px;text-align:right"><b>Diabetic Educator</b>a health professional who possesses knowledge of and experience in</div>
  <div class="node" style="left:835px;top:320px"><b>Nutritionists</b>an expert in dietetics, which includes human nutrition of diet</div>
  <div class="node" style="left:150px;top:440px;text-align:right"><b>Pedorthist</b>a professional who has special training in foot evaluation</div>
  <div class="node" style="left:845px;top:440px"><b>Podiatrist</b>a doctor qualified and trained to diagnose and treat conditions</div>
</section>

<section class="gov">
  <div class="gov-photo" role="img" aria-label="Photo of a patient speaking with a healthcare professional"></div>
  <div class="gov-box heading">Did you know that the government has setup programs to help educate, manage, and prevent your diabetes?</div>
  <div class="svc" style="left:310px;top:205px;width:522px;height:103px;padding:22px 20px 0 20px">
    <p style="width:300px"><span class="pink">DIABETIC SHOES</span> - the furnishing and fitting of either one pair of custom-molded shoes and inserts or one pair of extra-depth shoes each calendar year. Your plan also covers 2 additional pairs of inserts each calendar...</p>
    <span class="heading pink abs" style="right:20px;top:22px;font-size:14px">Pedorthist Services</span>
  </div>
  <div class="svc" style="left:572px;top:312px;width:428px;height:98px;padding:16px 16px 0 30px"><span class="chev">&lsaquo;</span><h4>Diabetic Educators</h4><p>a the furnishing and fitting of either one pair of custom-molded shoes and inserts or one pair of extra-depth shoes each calendar year.</p></div>
  <div class="svc" style="left:572px;top:414px;width:428px;height:98px;padding:16px 16px 0 30px"><span class="chev">&lsaquo;</span><h4>Nutritionists</h4><p>often abbreviated as MNT, is an evidence-based medical approach treating certain chronic conditions through the use</p></div>
  <div class="svc" style="left:572px;top:516px;width:428px;height:98px;padding:16px 16px 0 30px"><span class="chev">&lsaquo;</span><h4>Podiatrist</h4><p>podiatrist services such as foot exams every 6 months, foot injuries or diseases like hammer toes, bunion deformities, and heel spurs).</p></div>
</section>

<section class="newsletter">
  <div class="title heading">
    <svg width="56" height="52" viewBox="0 0 56 52"><path d="M4 20 L28 4 L52 20 V48 H4 Z" fill="none" stroke="#fff" stroke-width="3"/><path d="M4 20 L28 36 L52 20" fill="none" stroke="#fff" stroke-width="3"/><rect x="14" y="12" width="28" height="14" fill="#fff"/></svg>
    <span>Sign up for our<br>newsletter</span>
  </div>
  <div class="nl-field" style="left:498px;width:162px">First Name</div>
  <div class="nl-field" style="left:668px;width:162px">Last Name</div>
  <div class="nl-field" style="left:838px;width:162px">E-mail</div>
  <div class="nl-send">SEND</div>
</section>

<section class="pro">
  <div class="center-title heading" style="top:55px"><span class="sec-mark"></span><span class="pink">Healthcare Professional - Sign <span class="blue">up to be</span> part of <span class="blue">our network</span></span></div>
  <div class="field" style="left:200px;top:145px;width:190px">First Name</div>
  <div class="field" style="left:403px;top:145px;width:190px">Last Name</div>
  <div class="field" style="left:606px;top:145px;width:190px">Phone</div>
  <div class="field" style="left:809px;top:145px;width:191px">E-mail</div>
  <div class="field" style="left:303px;top:197px;width:190px">City</div>
  <div class="field" style="left:506px;top:197px;width:190px">State</div>
  <div class="field" style="left:709px;top:197px;width:190px">Zip Code</div>
  <div class="submit">SUBMIT</div>
</section>

<section class="blog">
  <div class="center-title heading" style="top:45px"><span class="sec-mark"></span><span class="pink">Our <span class="blue">Latest Blog</span></span></div>
  <article class="post" style="left:222px"><div class="post-date">Feb 5<br>2018<i></i></div><div class="post-img" role="img" aria-label="Blog photo of a glucose test"></div><h5>Lorem Ipsum is simply text</h5><p>Lorem Ipsum is simply dummy text of the printing and typesetting industry Lorem</p><div class="more"><span>Learn More</span></div></article>
  <article class="post" style="left:498px"><div class="post-date">Feb 5<br>2018<i></i></div><div class="post-img" role="img" aria-label="Blog photo of a couple reviewing health results"></div><h5>Lorem Ipsum is simply text</h5><p>Lorem Ipsum is simply dummy text of the printing and typesetting industry Lorem</p><div class="more"><span class="on">Learn More</span></div></article>
  <article class="post" style="left:775px"><div class="post-date">Feb 5<br>2018<i></i></div><div class="post-img" role="img" aria-label="Blog photo of a glucose test"></div><h5>Lorem Ipsum is simply text</h5><p>Lorem Ipsum is simply dummy text of the printing and typesetting industry Lorem</p><div class="more"><span>Learn More</span></div></article>
</section>

<footer class="footer">
  <div class="abs" style="left:200px;top:52px">&copy; Glucose Guidance Circle 2018<br>All Rights Reserved
    <div class="f-soc"><span style="background:var(--blue)"></span><span style="background:var(--pink)"></span><span style="background:var(--blue)"></span><span style="background:var(--pink)"></span></div>
  </div>
  <div class="abs" style="left:425px;top:50px">Site Map<br>Term &amp; Conditions<br>Privacy Policy<br>Help</div>
  <div class="abs" style="left:555px;top:50px"><h6>Keep in touch</h6>&#9990;&nbsp; +1 555 014 7788<br>&#9993;&nbsp; info@glucoseguidancecircle.example</div>
  <div class="abs" style="left:805px;top:50px;width:200px"><h6>Address</h6>&#8962;&nbsp; Lorem Ipsum is summy simple text industry..</div>
</footer>

</body>
</html>
```